Design a Label for a Line of Herbal Products

I am looking to hire a graphic designer for a long term project. I own a herbal shop and need new labels for my items. I am looking for labels with the color pink, must include photos of plants, text must be legible, must be modern.

I have attached documents from my business to provide as a guide for the type of look I am in search of.

Text: Seraphine Herbal Nest Tea
Subtext: Organic Loose herbs to support menstruation, strengthen the uterine wall and reduce menstrual flow.

Directions: Steep 1 tablespoon of herbal blend for 3-5 minutes. Allow to cool before drinking.
Solbrookwellnessarts.com

```html
<!DOCTYPE html>
<html lang="en">
<head>
<meta charset="utf-8">
<title>Seraphine Herbal Nest Tea – Label Set</title>
<link rel="stylesheet" href="https://fonts.googleapis.com/css2?family=Marcellus&family=Lora:wght@400&display=swap">
<style>
  :root {
    --page-bg: #ffffff;
    --label-pink: #f6b9c8;
    --gold: #c99a3e;
    --gold-light: #ecd08a;
    --ink: #3a2a2e;
    --brand-purple: #8a4a9c;
    --frond-dark: #2f7a2a;
    --frond-light: #8cc63f;
    --herb-green: #4f8f3a;
    --herb-amber: #d9a441;
  }
  * { box-sizing: border-box; margin: 0; padding: 0; }
  html, body {
    width: 1200px; height: 800px; overflow: hidden;
    background: var(--page-bg);
  }
  .sheet { position: relative; width: 1200px; height: 800px; }

  .label {
    position: absolute;
    background: var(--label-pink);
    overflow: hidden;
  }
  .label--square { left: 187px; top: 236px; width: 401px; height: 353px; }
  .label--round  { left: 656px; top: 206px; width: 414px; height: 414px; border-radius: 50%; }

  .fronds { position: absolute; inset: 0; width: 100%; height: 100%; }

  .panel {
    position: absolute;
    border: 2px solid var(--gold);
    box-shadow: inset 0 0 0 1px var(--gold-light);
    display: flex; flex-direction: column; align-items: center;
    text-align: center;
    padding: 8px 10px 0;
    color: var(--ink);
    font-family: "Lora", Georgia, serif;
  }
  .label--square .panel { left: 92px; top: 49px; width: 224px; height: 254px; }
  .label--round  .panel { left: 95px; top: 79px; width: 224px; height: 254px; }

  .brand { display: flex; flex-direction: column; align-items: center; gap: 3px; height: 50px; }
  .brand__dot { width: 30px; height: 30px; border-radius: 50%; background: var(--brand-purple); }
  .brand__name { font-size: 8px; color: var(--brand-purple); letter-spacing: 0.4px; }

  .product-name {
    font-family: "Marcellus", "Times New Roman", serif;
    font-weight: 400;
    font-size: 19px; line-height: 1.05; letter-spacing: 0.2px;
    margin-top: 18px; color: var(--ink);
  }
  .product-desc { font-size: 6.6px; line-height: 1.45; margin-top: 9px; max-width: 200px; }

  .herb-mark { margin-top: 7px; width: 32px; height: 20px; border-radius: 50%; }
  .herb-mark--blend { background: radial-gradient(circle, var(--herb-amber), var(--herb-green)); }
  .herb-mark--leaf  { background: linear-gradient(90deg, var(--herb-green), #2e6a23); width: 26px; height: 11px; margin-top: 10px; margin-bottom: 4px; }

  .directions { font-size: 5.4px; line-height: 1.6; margin-top: 7px; }
  .directions__title { font-size: 6.2px; margin-bottom: 1px; }
  .site { font-size: 6.4px; margin-top: 9px; }
</style>
</head>
<body>
<main class="sheet">

  <section class="label label--square" aria-label="Square tea label">
    <svg class="fronds" viewBox="0 0 401 353" aria-hidden="false">
      <defs>
        <linearGradient id="frondSq" x1="0" y1="0" x2="1" y2="1">
          <stop offset="0" stop-color="#8cc63f"/>
          <stop offset="1" stop-color="#2f7a2a"/>
        </linearGradient>
      </defs>
      <path role="img" aria-label="Palm frond" fill="url(#frondSq)" opacity="0.92"
            d="M150 22 C210 -4 300 -6 360 20 C385 32 398 50 400 70 L393 70 C382 50 350 34 300 26 C250 20 200 26 160 40 Z"/>
      <path role="img" aria-label="Palm frond" fill="url(#frondSq)" opacity="0.92"
            d="M8 88 C-4 150 10 240 60 300 C80 325 100 342 118 353 L92 353 C50 320 14 260 2 200 L0 110 Z"/>
    </svg>
    <div class="panel">
      <div class="brand"><span class="brand__dot"></span><span class="brand__name">Solbrook Wellness</span></div>
      <h1 class="product-name">SERAPHINE HERBAL<br>NEST TEA</h1>
      <p class="product-desc">Organic Loose herbs to support menstruation, strengthen the uterine wall and reduce menstrual flow.</p>
      <div class="herb-mark herb-mark--blend" role="img" aria-label="Herbs in a mortar"></div>
      <div class="directions">
        <p class="directions__title">Directions</p>
        <p>Steep 1 tablespoon of herbal blend for 3-5 minutes.</p>
        <p>Allow to cool before drinking.</p>
        <p>Solbrookwellnessarts.com</p>
      </div>
      <p class="site">Solbrookwellnessarts.com</p>
    </div>
  </section>

  <section class="label label--round" aria-label="Round tea label">
    <svg class="fronds" viewBox="0 0 414 414" aria-hidden="false">
      <defs>
        <linearGradient id="frondRd" x1="0" y1="0" x2="1" y2="1">
          <stop offset="0" stop-color="#8cc63f"/>
          <stop offset="1" stop-color="#2f7a2a"/>
        </linearGradient>
      </defs>
      <path role="img" aria-label="Palm frond" fill="url(#frondRd)" opacity="0.92"
            d="M196 28 C250 0 320 4 360 40 C390 70 405 110 412 150 L404 150 C394 112 376 80 346 56 C306 28 250 24 206 40 Z"/>
      <path role="img" aria-label="Palm frond" fill="url(#frondRd)" opacity="0.92"
            d="M30 120 C10 180 20 260 60 320 C80 350 104 372 130 388 L110 392 C72 364 34 318 16 260 C4 214 8 160 22 122 Z"/>
    </svg>
    <div class="panel">
      <div class="brand"><span class="brand__dot"></span><span class="brand__name">Solbrook Wellness</span></div>
      <h2 class="product-name">SERAPHINE HERBAL<br>NEST TEA</h2>
      <p class="product-desc">Organic Loose herbs to support menstruation, strengthen the uterine wall and reduce menstrual flow.</p>
      <div class="herb-mark herb-mark--leaf" role="img" aria-label="Mint leaves"></div>
      <div class="directions">
        <p class="directions__title">Directions</p>
        <p>Steep 1 tablespoon of herbal blend for 3-5 minutes.</p>
        <p>Allow to cool before drinking.</p>
        <p>Solbrookwellnessarts.com</p>
      </div>
      <p class="site">Solbrookwellnessarts.com</p>
    </div>
  </section>

</main>
</body>
</html>
```